Company Letter head for real estate company

need company letter head
Updates

You can use the logo that I submitted. no need to create a new one

Requirements
Must have
• must have my address on it..38264 WINDMERE, CANTON, MI 48302-1175, INFO@MUVRO.CA

```html
<!DOCTYPE html>
<html lang="en">
<head>
<meta charset="utf-8">
<title>Muvro Letterhead</title>
<link rel="stylesheet" href="https://fonts.googleapis.com/css2?family=Open+Sans:wght@300;400;600&family=Roboto:wght@300;400&family=Great+Vibes&display=swap">
<style>
  :root {
    --backdrop: #e4e4e4;
    --paper: #f1f1f1;
    --ink: #2b2b2b;
    --ink-soft: #555;
    --green-dark: #4e8a3a;
    --green-light: #7dba3e;
    --faint: #e2e2e2;
  }
  * { margin: 0; padding: 0; box-sizing: border-box; }
  html, body { width: 1200px; height: 1200px; overflow: hidden; background: var(--backdrop); }
  .letterhead {
    position: absolute; left: 204px; top: 40px;
    width: 792px; height: 1120px;
    background: var(--paper);
    box-shadow: 0 4px 14px rgba(0,0,0,0.12);
    font-family: "Open Sans", sans-serif;
    color: var(--ink);
  }
  .edge-bar { position: absolute; left: 0; width: 10px; background: var(--green-dark); }
  .edge-bar.top { top: 0; height: 989px; }
  .edge-bar.bottom { top: 1087px; height: 33px; }
  .edge-accent { position: absolute; left: 0; top: 993px; width: 18px; height: 89px; background: var(--green-light); }

  .brand {
    position: absolute; left: 0; right: 0; top: 66px;
    display: flex; justify-content: center; align-items: center; gap: 10px;
  }
  .brand-mark { width: 22px; height: 22px; border-radius: 50%; background: var(--green-light); }
  .brand-name { font-size: 34px; font-weight: 400; letter-spacing: 3px; color: var(--ink); }

  .letter-body {
    position: absolute; left: 129px; top: 262px; width: 579px;
    font-size: 12.6px; font-weight: 400; line-height: 18.7px; color: var(--ink);
  }
  .salutation { margin-bottom: 18.7px; }
  .letter-body p.paragraph { text-align: justify; margin-bottom: 18.7px; }
  .closing { position: absolute; left: 129px; top: 766px; font-size: 12.6px; }
  .signature {
    position: absolute; left: 134px; top: 790px;
    font-family: "Great Vibes", cursive; font-size: 30px; color: var(--ink);
  }

  .contact {
    position: absolute; left: 68px; top: 997px;
    font-family: "Roboto", sans-serif; font-weight: 300; font-size: 12.6px;
    color: var(--ink-soft); line-height: 16.2px;
  }
  .contact-line { display: flex; align-items: center; gap: 9px; }
  .contact-line svg { width: 10px; height: 10px; fill: var(--green-light); }
  .address { margin-top: 3px; }

  .scene-decoration {
    position: absolute; left: 309px; top: 925px; width: 483px; height: 195px;
    background: linear-gradient(180deg, rgba(226,226,226,0) 0%, var(--faint) 55%, #dedede 100%);
  }
</style>
</head>
<body>
  <div class="letterhead">
    <div class="edge-bar top"></div>
    <div class="edge-accent"></div>
    <div class="edge-bar bottom"></div>

    <div class="brand">
      <span class="brand-mark"></span>
      <span class="brand-name">MUVRO</span>
    </div>

    <div class="letter-body">
      <p class="salutation">Dear Daniel Hargrove,</p>
      <p class="paragraph">Lorem ipsum dolor sit amet, consectetuer adipiscing elit, sed diam nonummy nibh euismod tincidunt ut laoreet dolore magna aliquam erat volutpat. Ut wisi enim ad minim veniam, quis nostrud exerci tation ullamcorper suscipit lobortis nisl ut aliquip ex ea commodo consequat. Duis dolore te feugait nulla facilisi. Nam liber tempor cum soluta nobis eleifend option congue nihil imperdiet doming id quod mazim placerat facer possim assum. Lorem ipsum dolor sit amet, consectetuer adipiscing elit, sed diam nonummy nibh euismod tincidunt ut laoreet dolore magna aliquam erat volutpat. Ut wisi enim ad minim veniam, quis nostrud exerci tation ullamcorper suscipit lobortis nisl ut aliquip ex ea commodo consequat.</p>
      <p class="paragraph">Consectetuer adipiscing elit, sed diam nonummy nibh euismod tincidunt ut laoreet dolore magna aliquam erat volutpat. Ut wisi enim ad minim veniam, quis nostrud exerci tation ullamcorper suscipit lobortis nisl ut aliquip ex ea commodo consequat. Consectetuer adipiscing elit, sed diam nonummy nibh euismod tincidunt ut laoreet dolore magna aliquam erat volutpat. Ut wisi enim ad minim veniam, quis nostrud exerci tation ullamcorper suscipit lobortis nisl ut aliquip ex ea commodo consequat.</p>
      <p class="paragraph">Consectetuer adipiscing elit, sed diam nonummy nibh euismod tincidunt ut laoreet dolore magna aliquam erat volutpat. Ut wisi enim ad minim veniam, quis nostrud exerci tation ullamcorper suscipit lobortis nisl ut aliquip ex ea commodo consequat. Consectetuer adipiscing elit, sed diam nonummy nibh euismod tincidunt ut laoreet dolore magna aliquam erat volutpat. Ut wisi enim ad minim veniam, quis nostrud exerci tation ullamcorper suscipit lobortis nisl ut aliquip ex ea commodo consequat.</p>
    </div>

    <p class="closing">Sincerely Yours</p>
    <p class="signature">Thomas Kellerman</p>

    <div class="scene-decoration" role="img" aria-label="Faint illustration of trees and a house beside a winding path"></div>

    <div class="contact">
      <div class="contact-line">
        <svg viewBox="0 0 10 10"><path d="M2 0.5 L3.6 0.5 L4.2 2.8 L3.1 3.6 C3.6 4.9 5 6.3 6.4 6.9 L7.2 5.8 L9.5 6.4 L9.5 8 C9.5 8.9 8.8 9.5 8 9.5 C4 9.2 0.8 6 0.5 2 C0.5 1.2 1.1 0.5 2 0.5 Z"/></svg>
        <span>416.555.0148</span>
      </div>
      <div class="contact-line">
        <svg viewBox="0 0 10 10"><path d="M0.5 2 L9.5 2 L9.5 8 L0.5 8 Z M1.2 2.6 L5 5.4 L8.8 2.6" fill="none" stroke="#7dba3e" stroke-width="1"/></svg>
        <span>info@muvro.ca</span>
      </div>
      <div class="contact-line">
        <svg viewBox="0 0 10 10"><circle cx="5" cy="5" r="4.3" fill="none" stroke="#7dba3e" stroke-width="1"/><path d="M0.7 5 H9.3 M5 0.7 C2.8 3 2.8 7 5 9.3 M5 0.7 C7.2 3 7.2 7 5 9.3" fill="none" stroke="#7dba3e" stroke-width="0.8"/></svg>
        <span>www.muvro.ca</span>
      </div>
      <div class="address">38264 Windmere Dr<br>Canton, MI 48302-1175</div>
    </div>
  </div>
</body>
</html>
```